Quillmont Billboard - Financial Services Company (Investments, Tax Planning and Insurance)

Our new office has a billboard directly above the office building. We'd like something eye-catching with a strong Call to Action, with the main part of the billboard being under 7 words if possible. We'd like you to include a way to get ahold of us (either our website quillmontllc.example or our phone number 302-418-2267. You may also include in small font something to indicate that we've been serving the area since 1980 (the DE area, the tri-state area, the Ashgrove Hollow, etc.)

We offer financial planning, tax planning, and insurance, and we help our clients to focus on their goals and happiness by providing everything they need for lifelong wealth under one roof.

Our logos are attached, we use a triangle logo with green and gray. We use the tagline "experience lifelong wealth" but this does not need to be included.

Potential ideas we have seen from other financial companies-
- the concept that the driver spends more time looking at billboards than planning for their retirement
-something along the lines of "everything you need for your finances is in this building right here" planning, investments, taxes, insurance"
-don't spend your time worrying about retirement, let us help you plan for it
-are you working for your money, or is it working for you?
- retirement takes planning, we're here to help
- ready to retire? talk to us
- need investment advice?
- need help investing?
- crossing your fingers isn't a retirement plan. we can help.
- retiring soon? you need help.

Those are just general ideas, please feel free to be creative.

brand colors:
#00b585
#00b185
#000000
#ffffff
#6d6f75
#6d6f75
#6f7074
#021712
#052e24

```html
<!DOCTYPE html>
<html lang="en">
<head>
<meta charset="UTF-8">
<title>Quillmont Billboard</title>
<link rel="stylesheet" href="https://fonts.googleapis.com/css2?family=Montserrat:wght@800;900&display=swap">
<style>
  :root {
    --brand-green: #009d5e;
    --brand-gray: #6d6f75;
    --ink-white: #ffffff;
    --board-light: #f7fbf8;
    --board-mint: #aee3da;
    --page-bg: #eceff0;
    --photo-warm: #f3b3a6;
    --photo-cool: #b9bcbf;
  }
  html, body {
    margin: 0;
    padding: 0;
    width: 1200px;
    height: 900px;
    overflow: hidden;
    background: var(--page-bg);
  }
  .billboard {
    position: absolute;
    left: 40px;
    top: 205px;
    width: 1120px;
    height: 490px;
    display: block;
  }
  .brand-name {
    font-family: "Montserrat", sans-serif;
    font-weight: 800;
    font-size: 62px;
    fill: var(--brand-green);
  }
  .headline {
    font-family: "Montserrat", sans-serif;
    font-weight: 900;
    font-size: 66px;
    fill: var(--brand-gray);
  }
  .headline .accent { fill: var(--brand-green); }
  .headline-answer {
    font-family: "Montserrat", sans-serif;
    font-weight: 900;
    font-size: 64px;
    fill: var(--brand-green);
  }
  .cta-label, .cta-phone {
    font-family: "Montserrat", sans-serif;
    font-weight: 900;
    fill: var(--ink-white);
  }
  .cta-label { font-size: 32px; letter-spacing: 1px; }
  .cta-phone { font-size: 38px; }
</style>
</head>
<body>
<svg class="billboard" viewBox="0 0 1120 490" xmlns="http://www.w3.org/2000/svg" aria-label="Quillmont billboard">
  <defs>
    <linearGradient id="board-fill" x1="0" y1="0" x2="1" y2="0">
      <stop offset="0" stop-color="var(--board-light)"/>
      <stop offset="0.45" stop-color="#e6f5f1"/>
      <stop offset="1" stop-color="var(--board-mint)"/>
    </linearGradient>
    <linearGradient id="photo-fill" x1="0" y1="0" x2="1" y2="0.4">
      <stop offset="0" stop-color="var(--photo-warm)"/>
      <stop offset="0.55" stop-color="#eab9a3"/>
      <stop offset="1" stop-color="var(--photo-cool)"/>
    </linearGradient>
  </defs>

  <rect class="board-surface" width="1120" height="490" fill="url(#board-fill)"/>

  <polygon class="accent-band" points="654,490 867,0 1120,0 1120,490" fill="var(--brand-green)" opacity="0.92"/>

  <rect class="photo-area" x="680" y="150" width="440" height="270" rx="6" fill="url(#photo-fill)" role="img" aria-label="Open hand holding a pink piggy bank, grey patterned shirt sleeve"/>

  <g class="brand-lockup">
    <circle cx="165" cy="110" r="26" fill="var(--brand-green)"/>
    <text class="brand-name" x="212" y="132">Quillmont</text>
  </g>

  <text class="headline" x="43" y="246" textLength="607" lengthAdjust="spacingAndGlyphs">WORRYING ABOUT</text>
  <text class="headline" x="43" y="306">YOUR <tspan class="accent">$$$?</tspan></text>
  <text class="headline-answer" x="56" y="370" textLength="265" lengthAdjust="spacingAndGlyphs">US TOO!</text>

  <g class="cta-band">
    <polygon points="0,403 656,401 617,490 0,490" fill="var(--brand-gray)"/>
    <text class="cta-label" x="49" y="460">CALL US</text>
    <circle cx="273" cy="448" r="20" fill="var(--ink-white)"/>
    <path class="phone-icon" d="M265 437 c2-2 5-2 6 0 l3 5 c1 2 0 3-2 4 c1 3 3 5 6 6 c1-2 2-3 4-2 l5 3 c2 1 2 4 0 6 c-3 3-8 3-13-1 c-4-3-8-7-10-11 c-2-4-2-8 1-10z" fill="var(--brand-gray)"/>
    <text class="cta-phone" x="304" y="462" textLength="267" lengthAdjust="spacingAndGlyphs">302-418-2267</text>
  </g>
</svg>
</body>
</html>
```